Poster of Core Values & Motto

Create our core values poster and motto. Attached are our core values and our Motto. This poster represents both of our companies Tidy Pulp & CuraBinix.

Target Market(s)

Our team / employees

Industry/Entity Type

Shredding and Medical Waste

Colors
59FF00
82FF00
B8FF75
E3FFCB
F4FFEA
EB3D1F
EC4F4E
F09395
F8D3D4
FCEDEE

Requirements
Must have
• Include both companies logos

```html
<!DOCTYPE html>
<html lang="en">
<head>
<meta charset="utf-8">
<title>Core Values Poster – Tidy Pulp &amp; CuraBinix</title>
<link rel="stylesheet" href="https://fonts.googleapis.com/css2?family=Bebas+Neue&family=Open+Sans:wght@400;600;700&display=swap">
<style>
  :root {
    --green: #1fae4b;
    --green-light: #7cc242;
    --red: #e2312c;
    --ink: #111111;
    --text: #1d1d1d;
    --paper: #ffffff;
    --mist: #f3f4f4;
    --ring: #e9eaeb;
  }
  * { margin: 0; padding: 0; box-sizing: border-box; }
  html, body { width: 860px; height: 1200px; overflow: hidden; background: var(--paper); }
  .poster {
    position: relative; width: 860px; height: 1200px; overflow: hidden;
    background: linear-gradient(180deg, #fafafa 0%, #ffffff 60%);
    font-family: "Open Sans", Arial, sans-serif; color: var(--text);
  }
  .hero {
    position: absolute; left: 0; top: 118px; width: 860px; height: 450px;
    background:
      radial-gradient(ellipse 30% 35% at 50% 42%, #e4ecd8 0%, rgba(160,180,140,0.6) 45%, rgba(60,80,50,0) 100%),
      linear-gradient(180deg, #4c5e44 0%, #3c4a36 45%, #3a4431 70%, #2b3226 100%);
  }
  .header-band { position: absolute; left: 0; top: 0; width: 860px; height: 140px; }
  .brand {
    position: absolute; display: flex; align-items: center; gap: 12px;
    font-family: "Open Sans", Arial, sans-serif; font-weight: 700; white-space: nowrap;
  }
  .brand--pulp { left: 30px; top: 48px; font-size: 44px; color: var(--green); }
  .brand--pulp .brand-dot { width: 46px; height: 46px; border-radius: 50%; background: var(--green); }
  .brand--curabinix { right: 30px; top: 46px; font-size: 44px; color: var(--red); letter-spacing: 1px; }
  .banner { position: absolute; left: 279px; width: 314px; height: 48px; }
  .banner-title {
    position: absolute; inset: 0; display: flex; align-items: center; justify-content: center;
    font-family: "Bebas Neue", "Oswald", sans-serif; font-size: 36px; color: #fff; letter-spacing: 0.5px; padding-top: 3px;
  }
  .banner--top { top: 600px; }
  .banner--bottom { top: 1040px; }
  .values-diagram { position: absolute; left: 0; top: 680px; width: 860px; height: 330px; }
  .value { position: absolute; width: 240px; }
  .value h3 { font-size: 16.5px; font-weight: 700; letter-spacing: 0.6px; color: var(--ink); line-height: 1.2; white-space: nowrap; }
  .value p { font-size: 12.5px; line-height: 1.1; margin-top: 5px; color: var(--text); }
  .value--left { text-align: right; }
  .value--dependable { right: 598px; top: 702px; }
  .value--honesty { right: 653px; top: 820px; }
  .value--safe { right: 598px; top: 938px; }
  .value--synergy { left: 603px; top: 702px; }
  .value--excellence { left: 657px; top: 820px; }
  .value--efficient { left: 603px; top: 938px; }
  .motto {
    position: absolute; left: 0; width: 860px; top: 1100px; text-align: center;
    font-size: 23px; font-weight: 700; letter-spacing: 0.8px; color: var(--ink);
  }
  .tagline {
    position: absolute; left: 0; width: 860px; top: 1133px; text-align: center;
    font-size: 18px; font-weight: 400; color: var(--ink);
  }
  .footer-band { position: absolute; left: 0; bottom: 0; width: 860px; height: 32px; background: var(--green); }
</style>
</head>
<body>
<main class="poster">
  <div class="hero" role="img" aria-label="Photo of a young green tree growing on top of a mound of scrap and waste under a misty green sky"></div>

  <svg class="header-band" viewBox="0 0 860 140" aria-hidden="true">
    <path d="M0 0 H860 V110 H330 Q318 110 308 116 L290 124 Q282 130 270 130 H0 Z" fill="var(--paper)"/>
    <path d="M330 110 H860 V118 H320 Q322 112 330 110 Z" fill="var(--green)"/>
  </svg>

  <div class="brand brand--pulp"><span class="brand-dot"></span>Tidy Pulp</div>
  <div class="brand brand--curabinix">CuraBinix</div>

  <div class="banner banner--top">
    <svg width="314" height="48" viewBox="0 0 314 48" aria-hidden="true">
      <defs>
        <linearGradient id="bannerInk" x1="0" x2="1" y1="0" y2="0">
          <stop offset="0" stop-color="#0b0b0b"/><stop offset="0.5" stop-color="#2a2a2a"/><stop offset="1" stop-color="#0b0b0b"/>
        </linearGradient>
      </defs>
      <path d="M0 0 H297 L314 48 H17 Z" fill="url(#bannerInk)"/>
    </svg>
    <div class="banner-title">Our Core Values</div>
  </div>

  <svg class="values-diagram" viewBox="0 680 860 330" aria-hidden="true">
    <defs>
      <radialGradient id="iconDisc" cx="0.4" cy="0.35" r="0.7">
        <stop offset="0" stop-color="#3a3a3a"/><stop offset="1" stop-color="#050505"/>
      </radialGradient>
      <linearGradient id="recycleGreen" x1="0" y1="0" x2="1" y2="1">
        <stop offset="0" stop-color="#8fd14f"/><stop offset="1" stop-color="#3fa535"/>
      </linearGradient>
    </defs>
    <circle cx="431" cy="844" r="112" fill="var(--ring)"/>
    <circle cx="431" cy="844" r="132" fill="none" stroke="#111" stroke-width="1.2"/>
    <g stroke="#111" stroke-width="1.2">
      <line x1="301" y1="724" x2="333" y2="755"/><line x1="561" y1="724" x2="528" y2="755"/>
      <line x1="247" y1="844" x2="299" y2="844"/><line x1="617" y1="844" x2="563" y2="844"/>
      <line x1="301" y1="965" x2="333" y2="934"/><line x1="561" y1="965" x2="528" y2="934"/>
    </g>
    <g fill="#222">
      <circle cx="333" cy="755" r="3.5"/><circle cx="528" cy="755" r="3.5"/>
      <circle cx="299" cy="844" r="3.5"/><circle cx="563" cy="844" r="3.5"/>
      <circle cx="333" cy="934" r="3.5"/><circle cx="528" cy="934" r="3.5"/>
    </g>

    <g fill="url(#recycleGreen)" transform="translate(431 844) scale(1.3)">
      <g id="recycleArrow">
        <path d="M-26 -34 L-6 -52 Q0 -56 6 -52 L20 -34 L28 -40 L26 -14 L2 -20 L10 -26 L0 -40 L-12 -20 Z"/>
      </g>
      <use href="#recycleArrow" transform="rotate(120)"/>
      <use href="#recycleArrow" transform="rotate(240)"/>
    </g>

    <g fill="url(#iconDisc)" stroke="#fff" stroke-width="1.5">
      <circle cx="301" cy="724" r="29"/><circle cx="561" cy="724" r="29"/>
      <circle cx="247" cy="844" r="29"/><circle cx="617" cy="844" r="29"/>
      <circle cx="301" cy="965" r="29"/><circle cx="561" cy="965" r="29"/>
    </g>

    <g fill="#fff">
      <rect x="287" y="723" width="6" height="14" rx="1"/>
      <path d="M295 723 L301 714 Q302 708 305 708 Q309 709 307 716 L306 720 H314 Q317 721 316 724 L314 735 Q313 738 310 738 H295 Z"/>
    </g>
    <g fill="#fff">
      <circle cx="561" cy="716" r="5"/><path d="M551 735 Q551 723 561 723 Q571 723 571 735 Z"/>
      <circle cx="549" cy="719" r="3.8"/><path d="M541 733 Q541 724 549 724 Q554 724 555 727 L553 733 Z"/>
      <circle cx="573" cy="719" r="3.8"/><path d="M581 733 Q581 724 573 724 Q568 724 567 727 L569 733 Z"/>
    </g>
    <g fill="#fff">
      <path d="M247 845 L238 836 Q234 830 239 827 Q244 825 247 830 Q250 825 255 827 Q260 830 256 836 Z"/>
      <path d="M231 840 Q233 852 244 856 L244 860 L238 860 Q228 854 228 842 Z"/>
      <path d="M263 840 Q261 852 250 856 L250 860 L256 860 Q266 854 266 842 Z"/>
    </g>
    <g fill="none" stroke="#fff">
      <circle cx="612" cy="850" r="7" stroke-width="5" stroke-dasharray="3 2.5"/>
      <circle cx="612" cy="850" r="3" stroke-width="2"/>
      <circle cx="625" cy="836" r="5" stroke-width="3.5" stroke-dasharray="2.5 2"/>
      <circle cx="625" cy="836" r="2" stroke-width="1.5"/>
    </g>
    <g>
      <path d="M301 948 L315 953 V964 Q315 975 301 982 Q287 975 287 964 V953 Z" fill="none" stroke="#fff" stroke-width="2.5"/>
      <rect x="295" y="963" width="12" height="9" rx="1" fill="#fff"/>
      <path d="M297 963 V959 Q301 954 305 959 V963" fill="none" stroke="#fff" stroke-width="2"/>
    </g>
    <g fill="none" stroke="#fff" stroke-width="2">
      <circle cx="561" cy="965" r="15"/><circle cx="561" cy="965" r="9"/>
      <circle cx="561" cy="965" r="3" fill="#fff"/>
      <line x1="561" y1="945" x2="561" y2="985"/><line x1="541" y1="965" x2="581" y2="965"/>
    </g>
  </svg>

  <div class="value value--left value--dependable"><h3>DEPENDABLE</h3><p>Do what you say you will do</p></div>
  <div class="value value--left value--honesty"><h3>HONESTY/INTEGRITY</h3><p>Do the right thing</p></div>
  <div class="value value--left value--safe"><h3>SAFE AND SECURE</h3><p>We are just as secure as an<br>armored truck with money</p></div>
  <div class="value value--synergy"><h3>SYNERGY/TEAMWORK</h3><p>Get It Done Attitude with Humble<br>confidence</p></div>
  <div class="value value--excellence"><h3>EXCELLENCE</h3><p>Exceed expectations with<br>a smile</p></div>
  <div class="value value--efficient"><h3>EFFICIENT</h3><p>On-Time, sense of urgency, always<br>trying to improve</p></div>

  <div class="banner banner--bottom">
    <svg width="314" height="48" viewBox="0 0 314 48" aria-hidden="true">
      <path d="M0 0 H297 L314 48 H17 Z" fill="url(#bannerInk)"/>
    </svg>
    <div class="banner-title">Our Core Values</div>
  </div>

  <p class="motto">PURPOSE • CAUSE • PASSION</p>
  <p class="tagline">Remind people what great service looks like.</p>

  <div class="footer-band"></div>
</main>
</body>
</html>
```